■レイアウトの希望について
◎全体の左右のサイズは、1000px~1100pxくらいでお願いします。
※左右のサイドにナビを入れる場合は、左右300pxでお願いします。
◎現在のレイアウトは無視してください。
◎重要箇所を目立たせて、全体的にバランスよく配置させてください。
※重要箇所の順位は以下の通りです。
(1)検索ページへの入り口ブロック
(2)記事ページへのナビゲーション
(3)「イチオシ学生会館紹介サイト」と「オススメ学生会館」
(4)「学生会館以外のお部屋探し」
(5)「TOPICS」と「オススメ情報」
※見本のPDFは左ナビがあるようにレイアウトしていますが、トップページは2カラムにせず、1カラムでもかまいません。
(トップページに入れたいブロックを記載しただけですのでレイアウトの希望ではありません)
ただし、サブページは左右どちらかにナビを置く形の2カラムでお願いします。
(サブページのナビに入れるのは、記事ページへのナビゲーションと「学生会館以外のお部屋探し」のみです)

■デザインの希望について
◎落ち着いた感じのバランスの良いデザイン案が希望です。
※色数を多く使ったごちゃごちゃした配置は好みではありません。
※色は派手な感じでなく落ち着いた色が希望ですが、くすんだ色は好みではありません。
◎以前にタスクモアで依頼して作成した下記サイトもご参照ください。
http://www.sorahane-dorm.net/
http://www.qz7.net/
http://www.finerm.com/
http://222.xuu.jp/tomoya.net/
※一番下のみ現在作成中のため仮URLです。(全ページは完成していません)

■その他の希望について
◎ヘッダーはスマホサイズになった場合のことも考えて作成してください。
◎提案内で使用するイメージ画像は無料の素材サイトか、有料画像を使用する場合は、FOLMIOをご利用ください。
https://folmio-img.jp/
※現在サイト内にある画像を使用いただく形でもかまいません。

なお、初回のご提案はできるだけ締切日の2日前までにお願いします。
ギリギリの場合は修正依頼が間に合わず、候補になる良いご提案でも見送る場合がありますので..。

以上になりますので、ご提案のほど、よろしくお願いいたします。
http://www.heyanavi-dorm.net/
3ページ
基本的にはお任せですが、派手な色やくすんだ色は避けてください。(バランスの良い、落ち着いた色が希望)
• 高解像度JPG (.jpg)
• フォトショップ形式 (.psd)
JPG・PNGはどちらでもかまいません。
残り2日になりましたが、提案がないので締切日を延長いたします。

依頼詳細にも記載しましたが、できるだけ締切日の2日前までに初回のご提案をお送りいただけましたら幸いです。

その他、ご要望などがございましたら、メッセージからお送りください。
ロゴは現在のものは使用せず、見本と同様の一般的な横長のものを希望します。
(ロゴではなくて書体をそのまま使用する形でもかまいません)
弊社希望の「全体の左右のサイズは、1000px~1100pxくらい」とうのは、実際に文章や画像が入る本文(左右ナビが入る場合はその外側まで)のサイズになりますので、ご確認ください。

なお、すでにご提案を作成中の場合で、上記に当てはまらない場合はそのまま進めていただいてもかまいません。

とりあえず、デザインが分かれば問題ありませんので..。

※実際にお仕事を依頼することになった場合は、修正をお願いします。
お仕事が決まったあとに作成していただく、サブページのレイアウトを作成しましたので添付します。

決定したトップページと同じ方向性で、こちらのサブページも作成いただく形でお願いします。
今月末まで多忙になり、選考作業や細かい修正依頼作業がすぐにはできそうもないので、締切日をギリギリまで延ばさせていただきます。

必ず当選者は選定させていただきますので、よろしくお願いいたします。

また、依頼金額も若干アップさせていただきました。

全体的なバランスが良く、ごちゃごちゃしていなくて、統一感があり落ち着いた感じのご提案でした。

ご提案をいただき、ありがとうございました。
部分的には気に入ったご提案もあったのですが、全体的なバランスやメリハリといった点で、採用した案を選びました。
申し訳ございませんがご了承ください。
なお、今後も複数サイトのリニューアル依頼をタスクモアに出しますので、機会がございましたら、よろしくお願いいたします。

```html
<!DOCTYPE html>
<html lang="ja">
<head>
<meta charset="utf-8">
<title>学生会館ナビ</title>
<link href="https://fonts.googleapis.com/css2?family=Noto+Sans+JP:wght@400;500;700&display=swap" rel="stylesheet">
<style>
:root{
  --green:#8dc21f;
  --green-dark:#5e9a0c;
  --green-deep:#3f7a06;
  --green-pale:#eef6dc;
  --green-soft:#f6faef;
  --ink:#333;
  --ink-soft:#666;
  --line:#dcdcdc;
  --white:#fff;
  --accent:#e85a8c;
}
*{box-sizing:border-box;margin:0;padding:0}
html,body{width:1200px;height:2800px;overflow:hidden}
body{font-family:"Noto Sans JP",sans-serif;color:var(--ink);background:var(--white);font-size:13px;position:relative}
a{color:inherit;text-decoration:none}

/* header */
.site-header{height:120px;background:var(--white);display:flex;align-items:center;padding:0 24px;gap:24px;border-bottom:4px solid var(--green)}
.brand{display:flex;align-items:center;gap:10px;width:220px;font-size:22px;font-weight:700;color:var(--green-dark);white-space:nowrap}
.brand-dot{width:18px;height:18px;border-radius:50%;background:var(--green)}
.header-nav{display:flex;gap:12px}
.header-nav a{display:flex;align-items:center;height:46px;padding:0 18px;background:var(--green);color:var(--white);font-weight:700;font-size:15px;border-radius:4px;box-shadow:0 3px 0 var(--green-dark);white-space:nowrap}
.header-search{margin-left:auto;width:420px;border:1px solid var(--line);border-radius:4px;padding:10px 16px;text-align:center}
.header-search h2{font-size:14px;margin-bottom:6px}
.search-row{display:flex;justify-content:center;gap:6px}
.search-row input{width:240px;height:28px;border:1px solid #bbb;border-radius:3px;padding:0 8px;font-family:inherit;font-size:12px}
.search-row button{width:30px;height:28px;border:none;background:none}
.header-search p{font-size:11px;color:var(--ink-soft);margin-top:6px;white-space:nowrap}
.header-search p span{color:var(--accent)}

/* hero */
.hero{height:440px;position:relative;background:linear-gradient(180deg,#f3efe8 0%,#e8e0d4 55%,#d8cfc2 100%)}
.hero-photo{position:absolute;inset:0}
.hero-caption{position:absolute;left:0;right:0;bottom:22px;text-align:center;font-size:24px;font-weight:700;color:var(--ink)}
.hero-caption em{font-style:normal;color:var(--green-dark)}

/* search band */
.search-band{height:330px;background:var(--green);padding-top:30px}
.band-inner{width:760px;margin:0 auto}
.school-search{background:var(--white);border-radius:6px;padding:20px 30px;text-align:center}
.school-search h2{font-size:22px;margin-bottom:12px}
.school-search .search-row input{width:320px;height:34px}
.school-search .search-row button{height:34px}
.school-search p{font-size:12px;color:var(--ink-soft);margin-top:10px;white-space:nowrap}
.school-search p span{color:var(--accent)}
.band-buttons{display:flex;gap:20px;margin-top:30px}
.band-buttons a{flex:1;height:80px;background:var(--white);border-radius:6px;display:flex;align-items:center;justify-content:center;gap:14px;font-size:22px;font-weight:700;color:var(--green-deep);box-shadow:0 4px 0 var(--green-dark);white-space:nowrap}
.band-buttons .ico{width:44px;height:44px;border-radius:50%;background:var(--green);display:flex;align-items:center;justify-content:center}

/* article nav */
.article-nav{background:var(--green-pale);padding:36px 0 40px}
.card-grid{width:760px;margin:0 auto;display:grid;grid-template-columns:repeat(4,1fr);gap:18px}
.card{background:var(--white);border-radius:6px;height:190px;text-align:center;padding:18px 10px;box-shadow:0 2px 0 #d5e5b8}
.card .ico{width:56px;height:56px;border-radius:50%;background:var(--green);margin:0 auto 12px;display:flex;align-items:center;justify-content:center}
.card h3{font-size:13px;color:var(--green-deep);margin-bottom:8px;white-space:nowrap}
.card p{font-size:11px;color:var(--ink-soft);line-height:1.6}

/* main */
.main{width:760px;margin:56px auto 0;display:flex;gap:28px;align-items:flex-start}
.content{flex:1}
.block-title{font-size:18px;font-weight:700;padding:0 0 10px 12px;border-left:5px solid var(--green);border-bottom:2px solid var(--green);margin-bottom:10px}
.news-list{list-style:none;margin-bottom:110px}
.news-list li{display:flex;align-items:center;gap:10px;height:44px;border-bottom:1px dotted var(--line);font-size:13px}
.news-list li::before{content:"";width:0;height:0;border-left:6px solid var(--green);border-top:4px solid transparent;border-bottom:4px solid transparent}
.sidebar{width:196px}
.side-block{margin-bottom:26px}
.side-block h2{background:var(--green);color:var(--white);font-size:13px;text-align:center;padding:8px 0;border-radius:4px 4px 0 0;white-space:nowrap}
.side-block ul{list-style:none;border:1px solid var(--line);border-top:none;padding:8px}
.side-block li{height:54px;border:1px solid var(--line);margin-bottom:8px;display:flex;align-items:center;justify-content:center;gap:6px;font-size:14px;font-weight:700;color:var(--green-deep);background:var(--white);white-space:nowrap}
.side-block li:last-child{margin-bottom:0}
.side-block li i{width:10px;height:10px;background:var(--green)}
.side-block.rooms li{height:46px;background:var(--green-soft)}

/* footer */
.site-footer{position:absolute;left:0;right:0;bottom:0;height:300px}
.city{height:220px;background:linear-gradient(180deg,var(--white) 0%,#e4f1c9 50%,#a9d45a 100%)}
.footer-bar{height:80px;background:var(--green);color:var(--white);text-align:center;padding-top:18px;font-size:12px}
.footer-bar nav{display:flex;justify-content:center;gap:18px;margin-bottom:8px}
.footer-bar small{font-size:11px}
</style>
</head>
<body>
<header class="site-header">
  <div class="brand"><span class="brand-dot"></span>学生会館ナビ</div>
  <nav class="header-nav">
    <a href="#">路線から探す</a>
    <a href="#">地域から探す</a>
    <a href="#">食事付きを探す</a>
  </nav>
  <div class="header-search">
    <h2>学校名で探す</h2>
    <div class="search-row"><input type="text" placeholder="学校名を入力してください"><button aria-label="検索"><svg width="18" height="18" viewBox="0 0 18 18"><circle cx="7.5" cy="7.5" r="5.5" fill="none" stroke="#333" stroke-width="2"/><line x1="11.5" y1="11.5" x2="16" y2="16" stroke="#333" stroke-width="2.4"/></svg></button></div>
    <p>※通学予定の学校名を入力し <span>こちらから</span> 検索できます。</p>
  </div>
</header>

<section class="hero">
  <div class="hero-photo" role="img" aria-label="学生会館で笑顔で過ごす学生たちの写真"></div>
  <p class="hero-caption">一人暮らし希望の受験生にオススメの<em>「学生会館」</em>情報を満載</p>
</section>

<section class="search-band">
  <div class="band-inner">
    <div class="school-search">
      <h2>学校名で探す</h2>
      <div class="search-row"><input type="text" placeholder="学校名を入力してください"><button aria-label="検索"><svg width="22" height="22" viewBox="0 0 18 18"><circle cx="7.5" cy="7.5" r="5.5" fill="none" stroke="#333" stroke-width="2"/><line x1="11.5" y1="11.5" x2="16" y2="16" stroke="#333" stroke-width="2.4"/></svg></button></div>
      <p>※通学予定の大学・短大・専門学校・予備校名を入力してください。※該当がない場合は <span>エリアから検索</span> をご利用ください。</p>
    </div>
    <div class="band-buttons">
      <a href="#"><span class="ico"><svg width="22" height="22" viewBox="0 0 22 22"><rect x="5" y="3" width="12" height="13" rx="2" fill="#fff"/><rect x="7" y="5" width="8" height="5" fill="#8dc21f"/><line x1="7" y1="16" x2="4" y2="20" stroke="#fff" stroke-width="2"/><line x1="15" y1="16" x2="18" y2="20" stroke="#fff" stroke-width="2"/></svg></span>路線から探す</a>
      <a href="#"><span class="ico"><svg width="22" height="22" viewBox="0 0 22 22"><path d="M11 2a6 6 0 0 0-6 6c0 5 6 12 6 12s6-7 6-12a6 6 0 0 0-6-6z" fill="#fff"/><circle cx="11" cy="8" r="2.3" fill="#8dc21f"/></svg></span>地域から探す</a>
      <a href="#"><span class="ico"><svg width="22" height="22" viewBox="0 0 22 22"><line x1="7" y1="3" x2="7" y2="19" stroke="#fff" stroke-width="2"/><line x1="15" y1="3" x2="15" y2="19" stroke="#fff" stroke-width="2"/><path d="M4 3v5a3 3 0 0 0 6 0V3" fill="none" stroke="#fff" stroke-width="1.6"/></svg></span>食事付きを探す</a>
    </div>
  </div>
</section>

<section class="article-nav">
  <div class="card-grid">
    <a class="card" href="#"><span class="ico"><svg width="28" height="28" viewBox="0 0 28 28"><path d="M4 14 14 5l10 9v10H4z" fill="#fff"/></svg></span><h3>学生会館ってどんなところ？</h3><p>学生会館の特徴や、<br>寮との違いを解説します。</p></a>
    <a class="card" href="#"><span class="ico"><svg width="28" height="28" viewBox="0 0 28 28"><circle cx="10" cy="14" r="5" fill="none" stroke="#fff" stroke-width="2.5"/><line x1="15" y1="14" x2="24" y2="14" stroke="#fff" stroke-width="2.5"/></svg></span><h3>学生会館への入館</h3><p>入館の手続きと流れを<br>順番にご案内します。</p></a>
    <a class="card" href="#"><span class="ico"><svg width="28" height="28" viewBox="0 0 28 28"><circle cx="14" cy="14" r="9" fill="none" stroke="#fff" stroke-width="2.5"/><text x="14" y="19" font-size="12" text-anchor="middle" fill="#fff" font-family="sans-serif">¥</text></svg></span><h3>学生会館 VS アパート</h3><p>費用や暮らしやすさを<br>比べてみました。</p></a>
    <a class="card" href="#"><span class="ico"><svg width="28" height="28" viewBox="0 0 28 28"><rect x="6" y="5" width="16" height="19" rx="2" fill="#fff"/><line x1="9" y1="11" x2="19" y2="11" stroke="#8dc21f" stroke-width="2"/><line x1="9" y1="16" x2="19" y2="16" stroke="#8dc21f" stroke-width="2"/></svg></span><h3>実録 学生会館ルポ</h3><p>オススメの学生会館を<br>取材レポートします。</p></a>
    <a class="card" href="#"><span class="ico"><svg width="28" height="28" viewBox="0 0 28 28"><text x="14" y="19" font-size="11" font-weight="700" text-anchor="middle" fill="#fff" font-family="sans-serif">Q&amp;A</text></svg></span><h3>学生会館Q&amp;A</h3><p>よくある質問に<br>わかりやすくお答えします。</p></a>
    <a class="card" href="#"><span class="ico"><svg width="28" height="28" viewBox="0 0 28 28"><rect x="6" y="10" width="16" height="13" rx="2" fill="#fff"/><path d="M9 10V7a5 5 0 0 1 10 0v3" fill="none" stroke="#fff" stroke-width="2.2"/></svg></span><h3>保護者の方へ</h3><p>安心の設備とサポート<br>について紹介します。</p></a>
    <a class="card" href="#"><span class="ico"><svg width="28" height="28" viewBox="0 0 28 28"><circle cx="14" cy="14" r="9" fill="none" stroke="#fff" stroke-width="2.5"/><path d="M14 8v6l4 3" fill="none" stroke="#fff" stroke-width="2.2"/></svg></span><h3>学生会館の一日</h3><p>入館生の一日の<br>過ごし方をご紹介します。</p></a>
    <a class="card" href="#"><span class="ico"><svg width="28" height="28" viewBox="0 0 28 28"><path d="M7 14l5 5 9-10" fill="none" stroke="#fff" stroke-width="3"/></svg></span><h3>学生会館の選び方</h3><p>失敗しない選び方の<br>ポイントをまとめました。</p></a>
  </div>
</section>

<div class="main">
  <div class="content">
    <h2 class="block-title">TOPICS</h2>
    <ul class="news-list">
      <li>学生会館情報館 一人暮らし情報を受験生向けに公開</li>
      <li>一人暮らしに役立つ資料の無料プレゼント 受付中</li>
      <li>学生マンションの比較・検討情報（大学の近くにあります）</li>
      <li>食事付き学生会館の特集ページを更新しました</li>
      <li>春の新生活準備ガイドを掲載しました</li>
      <li>オススメ学生会館ルポ 第三回を公開</li>
      <li>保護者向けの安心ガイドを追加しました</li>
      <li>入館申込の受付スケジュールのお知らせ</li>
    </ul>
    <h2 class="block-title">オススメ情報</h2>
    <ul class="news-list">
      <li>学生マンション資料請求 一括比較</li>
      <li>学生会館を最短で探す方法</li>
      <li>食事付き学生会館の選び方ガイド</li>
      <li>新生活の家具家電の準備リスト</li>
      <li>女子学生専用の会館特集</li>
    </ul>
  </div>
  <aside class="sidebar">
    <section class="side-block">
      <h2>イチオシ学生会館紹介サイト</h2>
      <ul><li><i></i>はるかぜ学生会館</li><li><i></i>そよかぜ学生寮</li><li><i></i>こだま会館案内</li></ul>
    </section>
    <section class="side-block">
      <h2>オススメ学生会館</h2>
      <ul><li><i></i>みどり野学生会館</li><li><i></i>ひなた学生寮</li><li><i></i>あおば学生会館</li></ul>
    </section>
    <section class="side-block rooms">
      <h2>学生会館以外のお部屋探し</h2>
      <ul><li>こもれび賃貸</li><li>ふたば住まい探し</li><li>みずほ下宿案内</li><li>つばさ寮ナビ</li><li>ひかりシェア住まい</li><li>いろは部屋さがし</li></ul>
    </section>
  </aside>
</div>

<footer class="site-footer">
  <div class="city" role="img" aria-label="緑色の街並みのシルエットイラスト"></div>
  <div class="footer-bar">
    <nav><a href="#">運営会社</a><a href="#">プライバシーポリシー</a><a href="#">サイトマップ</a><a href="#">お問い合わせ</a></nav>
    <small>Copyright © 学生会館ナビ All Rights Reserved.</small>
  </div>
</footer>
</body>
</html>
```